We need banner ads in different sizes for a boat sales event on Pine Hollow Reservoir, OK. People will need to go to 5 different locations and they have the option if they go to all the stops of winning a $2000 tropical travel voucher. Most of the boats are 30' yachts such as WaveKin, Cresta, Tidelmark, Dell Vantor brands plus jet ski.

Please do not use more than 7 elements.
Name - Sail Ahead Open-Dock Boat Fair
April 29-May 1st
Pine Hollow Reservoir, Oklahoma
Over 100 new and pre-owned boats at 5 locations and 7 boat dealers

Standard Ad Unit Sizes – W X H
Inline Rectangle
300 X 250
Leaderboard
728 X 90
Large Rectangle
336 X 280
Wide Skyscraper
160 X 600
Banner
468 X 60
Skyscraper
120 X 600
Square
250 X 250
Small Square
200 X 200

· Maximum file size is 150KB for each ad.

· Acceptable file types for non-animated ads: .jpg (my preferred), .png and .gif

Target Market(s)

Men in their 30-50 Range

Industry/Entity Type

Event

Font styles to use
Serif

Colors
0255a3
85cae6
33b8a4

Requirements
Must have
• Logo, Date, Boat or nautical element and win a tropical travel voucher
Nice to have
• Map of locations
Should not have
• Does not need to have website on the ad

```html
<!DOCTYPE html>
<html lang="en">
<head>
<meta charset="utf-8">
<title>Sail Ahead Open-Dock Boat Fair – Banner Frames</title>
<link rel="stylesheet" href="https://fonts.googleapis.com/css2?family=Bebas+Neue&display=swap">
<style>
  :root {
    --page: #ffffff;
    --ink: #1c1c1c;
    --teal: #1a9aad;
    --cream: #efe7b8;
    --gold: #f7df8a;
    --mint: #d3ebb0;
    --pink: #f3acd6;
    --white: #ffffff;
    --navy: #0b3f66;
    --button-top: #f6e2a0;
    --button-bottom: #d9b965;
  }
  * { box-sizing: border-box; margin: 0; padding: 0; }
  html, body {
    width: 1200px; height: 1050px; overflow: hidden;
    background: var(--page);
    font-family: "Bebas Neue", "Arial Narrow", sans-serif;
  }
  .board { position: relative; width: 1200px; height: 1050px; }

  .frame-label {
    position: absolute; width: 450px; text-align: center;
    font-size: 24px; letter-spacing: 0.5px; color: var(--ink);
  }

  .ad {
    position: absolute; width: 450px; height: 375px; overflow: hidden;
    background: var(--teal);
  }
  .ad--one   { left: 110px; top: 122px; }
  .ad--two   { left: 635px; top: 122px; }
  .ad--three { left: 374px; top: 591px; }

  .ad__photo { position: absolute; left: 0; top: 0; width: 450px; height: 230px; }
  .photo--kids  { background: linear-gradient(180deg, #e9eef0 0%, #f1f1ee 45%, #d9d1c2 70%, #c9bfae 100%); }
  .photo--boat  { background: linear-gradient(180deg, #c9ccd0 0%, #8e97a3 40%, #3f4e66 65%, #9ea7b0 100%); }
  .photo--coast { background: linear-gradient(180deg, #59a9e3 0%, #a7d3ef 40%, #e6f3f8 55%, #3cc3cf 70%, #62d6d3 100%); }

  .ad__wave { position: absolute; left: 0; top: 0; width: 450px; height: 375px; }

  .ad__brand {
    position: absolute; right: 16px; top: 12px;
    display: flex; align-items: center; gap: 8px;
    color: var(--navy); font-size: 22px; line-height: 0.95; text-align: right;
  }
  .ad__brand-dot { width: 14px; height: 14px; border-radius: 50%; background: var(--navy); }

  .ad__copy {
    position: absolute; left: 20px; right: 20px;
    text-align: center; color: var(--white);
    font-size: 34px; line-height: 1.22; letter-spacing: 0.3px;
  }
  .ad--one .ad__copy { top: 218px; font-size: 30px; line-height: 1.18; }
  .ad--two .ad__copy { top: 230px; }
  .ad--three .ad__copy { top: 228px; }

  .hl-gold { color: var(--gold); }
  .hl-mint { color: var(--mint); }
  .hl-pink { color: var(--pink); }

  .ad__button {
    position: absolute; left: 155px; top: 320px; width: 141px; height: 40px;
    border-radius: 4px;
    background: linear-gradient(180deg, var(--button-top), var(--button-bottom));
    color: var(--teal); font-size: 26px; line-height: 42px; text-align: center;
  }
</style>
</head>
<body>
<main class="board">

  <div class="frame-label" style="left:110px; top:72px;">Frame 1</div>
  <div class="frame-label" style="left:635px; top:72px;">Frame 2</div>
  <div class="frame-label" style="left:374px; top:541px;">Frame 3</div>

  <section class="ad ad--one">
    <div class="ad__photo photo--kids" role="img" aria-label="Photo of two children in life jackets playing on a pontoon boat seat"></div>
    <svg class="ad__wave" viewBox="0 0 450 375" aria-hidden="true">
      <path d="M0,178 Q225,232 450,178 L450,375 L0,375 Z" fill="var(--cream)"/>
      <path d="M0,196 Q225,232 450,196 L450,375 L0,375 Z" fill="var(--teal)"/>
    </svg>
    <div class="ad__brand"><span class="ad__brand-dot"></span><span>Sail Ahead<br>Boat Fair</span></div>
    <p class="ad__copy">Sail Ahead Open-Dock Boat Fair sets sail on <span class="hl-gold">Pine Hollow Reservoir,</span> <span class="hl-mint">OK. April 29th - May 1st</span></p>
  </section>

  <section class="ad ad--two">
    <div class="ad__photo photo--boat" role="img" aria-label="Photo of a pontoon boat cruising on open water"></div>
    <svg class="ad__wave" viewBox="0 0 450 375" aria-hidden="true">
      <path d="M0,178 Q225,232 450,178 L450,375 L0,375 Z" fill="var(--cream)"/>
      <path d="M0,196 Q225,232 450,196 L450,375 L0,375 Z" fill="var(--teal)"/>
    </svg>
    <div class="ad__brand"><span class="ad__brand-dot"></span><span>Sail Ahead<br>Boat Fair</span></div>
    <p class="ad__copy"><span class="hl-gold">Over 100</span> new and pre-owned boats at <span class="hl-mint">5 locations</span> and <span class="hl-gold">7</span> <span class="hl-pink">boat dealers</span></p>
  </section>

  <section class="ad ad--three">
    <div class="ad__photo photo--coast" role="img" aria-label="Photo of yachts anchored in a turquoise tropical bay"></div>
    <svg class="ad__wave" viewBox="0 0 450 375" aria-hidden="true">
      <path d="M0,178 Q225,232 450,178 L450,375 L0,375 Z" fill="var(--cream)"/>
      <path d="M0,196 Q225,232 450,196 L450,375 L0,375 Z" fill="var(--teal)"/>
    </svg>
    <div class="ad__brand"><span class="ad__brand-dot"></span><span>Sail Ahead<br>Boat Fair</span></div>
    <p class="ad__copy">Win a <span class="hl-gold">tropical travel<br>voucher</span> for <span class="hl-pink">$2000</span></p>
    <div class="ad__button">More Info</div>
  </section>

</main>
</body>
</html>
```